cycle trainer

Designing an vexo app that will offer multiple videos for indoor cycle training. On start up users will be shown a grid categorised by locations and types of training such as cycle for 30 mins or an hour in xyz locations. Once the user selects a training video a full screen video will play on the screen with an overlay showing the cycling speed, cadence, distance and heart rate along with a timer obtained through bluetooth accessories attached to the stationary bike. Once the video concludes a summary of workout will be displayed showing average speed, cadence, calories burned and distance covered. The user will have the opportunity to save the workout. Saved workouts can be retrieved through the workout history tab where a graph will show the captured averages.
A blueprint is attached, i am looking for is style flat translucent design if possible with large images and images cropped out
Training

```html
<!DOCTYPE html>
<html lang="en">
<head>
<meta charset="utf-8">
<title>CycleTrainer Application</title>
<link href="https://fonts.googleapis.com/css2?family=Arimo:wght@400;700&display=swap" rel="stylesheet">
<style>
:root{
  --page:#eef0f2;
  --bar:#f7f7f7;
  --ink:#111111;
  --accent:#1a7ae8;
  --label:#ffffff;
  --icon:#1e1e1e;
  --dot:#ffffff;
  --sky:#e3e7ea;
  --field:#c9cf9b;
  --road:#b9b6b0;
  --fence:#c6cbc9;
  --wall:#b8b8b2;
}
*{box-sizing:border-box;margin:0;padding:0}
html,body{width:1200px;height:874px;overflow:hidden;background:var(--page);font-family:"Arimo",Arial,sans-serif;color:var(--ink)}
.screen{position:absolute;left:41px;top:17px;width:916px;height:688px;transform:scale(1.22);transform-origin:0 0;overflow:hidden;background:#fff;box-shadow:0 2px 12px rgba(0,0,0,.15)}
.status{height:20px;background:var(--bar);display:flex;align-items:center;justify-content:space-between;padding:0 6px;font-size:11px}
.status .time{position:absolute;left:0;right:0;text-align:center;pointer-events:none}
.battery{display:inline-flex;align-items:center;gap:4px}
.battery i{display:inline-block;width:22px;height:10px;background:var(--ink);border-radius:2px}
.navbar{position:relative;height:35px;background:var(--bar);display:flex;align-items:center;justify-content:space-between;padding:0 16px 0 25px;border-bottom:1px solid #ddd}
.navbar h1{position:absolute;left:0;right:0;text-align:center;font-size:15px;font-weight:700;pointer-events:none}
.nav-icons{display:flex;gap:8px}
.content{position:relative;height:633px}
.backdrop{position:absolute;inset:0;background:
  linear-gradient(90deg,rgba(0,0,0,0) 65%,rgba(40,90,160,.55) 75%,rgba(40,90,160,.2) 100%),
  linear-gradient(180deg,#c9ccce 0%,#b6bcc2 35%,#c9ad8e 60%,#d3b292 100%)}
.free-band{position:absolute;left:0;right:0;top:410px;bottom:0;background:rgba(245,215,185,.45);border-top:1px solid rgba(255,255,255,.5)}
.grid{position:absolute;left:24px;display:grid;grid-template-columns:repeat(4,202px);column-gap:20px}
.grid.paid{top:22px;row-gap:14px}
.grid.free{top:451px}
.tile{background:var(--label);box-shadow:0 1px 4px rgba(0,0,0,.2)}
.thumb{position:relative;height:150px;display:flex;align-items:center;justify-content:center}
.free .thumb{height:147px}
.thumb.road{background:linear-gradient(180deg,var(--sky) 0%,var(--sky) 38%,var(--field) 55%,var(--road) 100%)}
.thumb.fence{background:linear-gradient(180deg,var(--fence) 0%,var(--fence) 45%,var(--wall) 60%,#a9a9a6 100%)}
.thumb.faded::after{content:"";position:absolute;inset:0;background:rgba(255,255,255,.35)}
.thumb svg{position:relative;z-index:1}
.progress{position:absolute;left:0;bottom:0;width:150px;height:6px;background:var(--accent)}
.title{height:29px;line-height:29px;padding-left:10px;font-size:14.5px;font-weight:700}
.free .title{height:25px;line-height:25px}
.section-head{position:absolute;left:27px;top:419px;font-size:20px;font-weight:700}
.pager{position:absolute;left:897px;top:185px;display:flex;flex-direction:column;gap:6px}
.pager span{width:12px;height:12px;border-radius:50%;background:var(--dot)}
.pager span.on{background:var(--accent)}
</style>
</head>
<body>
<main class="screen">
  <div class="status">
    <span>vexo</span>
    <span class="time">4:21 PM</span>
    <span class="battery">100% <i></i></span>
  </div>
  <header class="navbar">
    <svg width="17" height="16" viewBox="0 0 17 16" aria-label="Menu"><rect y="1" width="17" height="3" fill="#1a7ae8"/><rect y="7" width="17" height="3" fill="#1a7ae8"/><rect y="13" width="17" height="3" fill="#1a7ae8"/></svg>
    <h1>CycleTrainer Application</h1>
    <div class="nav-icons">
      <svg width="22" height="20" viewBox="0 0 22 20" aria-label="Settings"><circle cx="8" cy="11" r="6" fill="none" stroke="#1a7ae8" stroke-width="4" stroke-dasharray="3 2"/><circle cx="8" cy="11" r="2" fill="#1a7ae8"/><circle cx="17" cy="5" r="3.5" fill="none" stroke="#1a7ae8" stroke-width="2.5" stroke-dasharray="2 1.5"/></svg>
      <svg width="20" height="20" viewBox="0 0 20 20" aria-label="Profile"><circle cx="10" cy="6" r="5" fill="#1a7ae8"/><path d="M0 20c0-6 4-8 10-8s10 2 10 8z" fill="#1a7ae8"/></svg>
    </div>
  </header>

  <section class="content">
    <div class="backdrop" role="img" aria-label="Blurred cycling photograph as backdrop"></div>
    <div class="free-band"></div>

    <div class="grid paid">
      <article class="tile"><div class="thumb road" role="img" aria-label="Cyclists riding a country road"><div class="progress"></div></div><div class="title">Basic Training 1</div></article>
      <article class="tile"><div class="thumb fence faded" role="img" aria-label="Cyclist passing an iron fence"><svg width="60" height="52" viewBox="0 0 60 52"><path d="M0 4h9l8 30h34l7-24H14" fill="none" stroke="#1e1e1e" stroke-width="4"/><path d="M15 13h40l-5 18H20z" fill="#1e1e1e"/><circle cx="22" cy="45" r="5" fill="#1e1e1e"/><circle cx="46" cy="45" r="5" fill="#1e1e1e"/></svg></div><div class="title">Basic Training 1</div></article>
      <article class="tile"><div class="thumb road faded" role="img" aria-label="Cyclists riding a country road"><svg width="60" height="52" viewBox="0 0 60 52"><path d="M0 4h9l8 30h34l7-24H14" fill="none" stroke="#1e1e1e" stroke-width="4"/><path d="M15 13h40l-5 18H20z" fill="#1e1e1e"/><circle cx="22" cy="45" r="5" fill="#1e1e1e"/><circle cx="46" cy="45" r="5" fill="#1e1e1e"/></svg></div><div class="title">Basic Training 1</div></article>
      <article class="tile"><div class="thumb fence faded" role="img" aria-label="Cyclist passing an iron fence"><svg width="60" height="52" viewBox="0 0 60 52"><path d="M0 4h9l8 30h34l7-24H14" fill="none" stroke="#1e1e1e" stroke-width="4"/><path d="M15 13h40l-5 18H20z" fill="#1e1e1e"/><circle cx="22" cy="45" r="5" fill="#1e1e1e"/><circle cx="46" cy="45" r="5" fill="#1e1e1e"/></svg></div><div class="title">Basic Training 1</div></article>
      <article class="tile"><div class="thumb road faded" role="img" aria-label="Cyclists riding a country road"><svg width="60" height="52" viewBox="0 0 60 52"><path d="M0 4h9l8 30h34l7-24H14" fill="none" stroke="#1e1e1e" stroke-width="4"/><path d="M15 13h40l-5 18H20z" fill="#1e1e1e"/><circle cx="22" cy="45" r="5" fill="#1e1e1e"/><circle cx="46" cy="45" r="5" fill="#1e1e1e"/></svg></div><div class="title">Basic Training 1</div></article>
      <article class="tile"><div class="thumb fence faded" role="img" aria-label="Cyclist passing an iron fence"><svg width="60" height="52" viewBox="0 0 60 52"><path d="M0 4h9l8 30h34l7-24H14" fill="none" stroke="#1e1e1e" stroke-width="4"/><path d="M15 13h40l-5 18H20z" fill="#1e1e1e"/><circle cx="22" cy="45" r="5" fill="#1e1e1e"/><circle cx="46" cy="45" r="5" fill="#1e1e1e"/></svg></div><div class="title">Basic Training 1</div></article>
      <article class="tile"><div class="thumb road faded" role="img" aria-label="Cyclists riding a country road"><svg width="60" height="52" viewBox="0 0 60 52"><path d="M0 4h9l8 30h34l7-24H14" fill="none" stroke="#1e1e1e" stroke-width="4"/><path d="M15 13h40l-5 18H20z" fill="#1e1e1e"/><circle cx="22" cy="45" r="5" fill="#1e1e1e"/><circle cx="46" cy="45" r="5" fill="#1e1e1e"/></svg></div><div class="title">Basic Training 1</div></article>
      <article class="tile"><div class="thumb fence faded" role="img" aria-label="Cyclist passing an iron fence"><svg width="60" height="52" viewBox="0 0 60 52"><path d="M0 4h9l8 30h34l7-24H14" fill="none" stroke="#1e1e1e" stroke-width="4"/><path d="M15 13h40l-5 18H20z" fill="#1e1e1e"/><circle cx="22" cy="45" r="5" fill="#1e1e1e"/><circle cx="46" cy="45" r="5" fill="#1e1e1e"/></svg></div><div class="title">Basic Training 1</div></article>
    </div>

    <nav class="pager" aria-label="Pages"><span class="on"></span><span></span><span></span><span></span></nav>

    <h2 class="section-head">Free content</h2>
    <div class="grid free">
      <article class="tile"><div class="thumb road faded" role="img" aria-label="Cyclists riding a country road"><svg width="40" height="44" viewBox="0 0 40 44"><path d="M0 0l40 22L0 44z" fill="#1e1e1e"/></svg></div><div class="title">Basic Training 1</div></article>
      <article class="tile"><div class="thumb fence faded" role="img" aria-label="Cyclist passing an iron fence"><svg width="40" height="44" viewBox="0 0 40 44"><path d="M0 0l40 22L0 44z" fill="#1e1e1e"/></svg></div><div class="title">Basic Training 1</div></article>
      <article class="tile"><div class="thumb road faded" role="img" aria-label="Cyclists riding a country road"><svg width="40" height="44" viewBox="0 0 40 44"><path d="M0 0l40 22L0 44z" fill="#1e1e1e"/></svg></div><div class="title">Basic Training 1</div></article>
      <article class="tile"><div class="thumb fence faded" role="img" aria-label="Cyclist passing an iron fence"><svg width="40" height="44" viewBox="0 0 40 44"><path d="M0 0l40 22L0 44z" fill="#1e1e1e"/></svg></div><div class="title">Basic Training 1</div></article>
    </div>
  </section>
</main>
</body>
</html>
```